Automotive Mechanic Website Design

We are working with an auto repair shop in California.
A few websites for inspiration:
https://brindlecovemotors.example
https://www.folionest.example/gallery/57316284/Torvane-Auto-Services-Repair-SiteKit-Theme
http://www.quelbrightmotors.example
https://www.halvikgarage.example
https://www.pdmotorhaus.example
Thank you for taking the time to consider designing a website for us. We are web developers based in Stockton, CA, USA. Most of our projects go through the same process. Understanding this process may help you win a project with us. We custom-code all of our websites in-house. We don’t have any requirements as to what tools you use for your design, but we ask that you follow these guidelines.
IMAGES:
If you use any images or icons in the design, we ask that you have a link to the asset so we can purchase the image/icon. Most of the designs we submit do not have the customer’s images on them unless they have some great images. Be creative; show us the feeling you are trying to portray with your image choices. Use any royalty-free site you choose. We subscribe to Adobe and mainly use their images, but we can purchase images outside of Adobe. PLEASE NOTE: we will not submit designs to clients with watermarks on the images.
FONTS:
We ask that you identify the fonts you’re using in the design. This can be done in a message if you want. We typically use Google Fonts and Adobe Fonts.
CONTENT:
We're always open to different content and ideas. We often submit designs with stock images so the client can see our vision. We typically take pictures after the website launch to use their images with our vision. Lorem Ipsum is fine for paragraphs, but we ask that you make the Headers with correct English. We want to be able to show the vision and identify the sections of the website.
INSPIRATION:
We typically add a couple of links in the brief of websites we like to help you get started in your design.
REVISIONS:
We do not often ask for revisions of the designs unless we see something in the design that may not appeal to the client. If there are slight changes that we want to make, we do that in the development process.
FEEDBACK:
We rarely give feedback on designs during the design process. We are working on many website projects and do not have the time to provide feedback. We usually respond if your request is well thought out and asks specific questions, but a note asking “feedback, please” usually goes unanswered.

```html
<!DOCTYPE html>
<html lang="en">
<head>
<meta charset="utf-8">
<title>Corvex Auto Repair</title>
<link href="https://fonts.googleapis.com/css2?family=Roboto:ital,wght@0,400;0,500;0,700;0,900;1,400&family=Open+Sans:ital,wght@0,400;0,600;1,400&display=swap" rel="stylesheet">
<style>
:root{
  --red:#f2262f;
  --navy:#050a1c;
  --ink:#151515;
  --grey:#4a4a4a;
  --light:#f4f4f4;
  --white:#ffffff;
}
*{box-sizing:border-box;margin:0;padding:0}
html,body{width:1200px;height:4313px;overflow:hidden}
body{position:relative;background:var(--white);font-family:"Open Sans",Arial,sans-serif;color:var(--ink)}
.abs{position:absolute}
.head{font-family:"Roboto",Arial,sans-serif;font-weight:700;text-transform:uppercase;line-height:1}
.head .hl{color:var(--red)}
.photo{position:absolute}
.btn{position:absolute;display:flex;align-items:center;justify-content:center;font-family:"Roboto",Arial,sans-serif;font-weight:500;color:var(--white);background:var(--red);border-radius:30px;text-transform:uppercase}
/* header */
.topbar{left:0;top:0;width:1200px;height:4px;background:var(--navy)}
.brand{font-family:"Roboto",Arial,sans-serif;font-weight:900;color:var(--red);font-size:30px;letter-spacing:1px;line-height:1}
.brand small{display:block;font-size:14px;color:var(--ink);letter-spacing:0.5px;margin-top:4px;text-align:right}
.nav{left:524px;top:80px;display:flex;gap:0;font-family:"Roboto",Arial,sans-serif;font-size:14px;text-transform:uppercase;color:var(--ink)}
.nav span{position:absolute;white-space:nowrap}
/* hero */
.hero-red{left:0;top:109px;width:420px;height:547px;background:var(--red)}
.hero-photo{left:420px;top:109px;width:780px;height:547px;background:linear-gradient(120deg,#3a3f4a,#1f2a4a 45%,#b0281f 75%,#5a1a14)}
.hero-title{left:149px;top:242px;font-size:50px;color:var(--white);line-height:61px}
.hero-btn{left:149px;top:452px;width:331px;height:53px;background:var(--navy);border:3px solid var(--white);font-size:22px;font-weight:700}
/* about */
.dots{left:149px;top:765px;width:161px;height:164px;background-image:radial-gradient(#bbb 1.2px,transparent 1.3px);background-size:8px 8px}
.about-big{left:219px;top:815px;width:382px;height:318px;background:linear-gradient(135deg,#d9dadd,#8d9096 55%,#2c2d31)}
.about-small{left:149px;top:1036px;width:187px;height:162px;background:linear-gradient(135deg,#2a1013,#b3121c 60%,#4a0a0e)}
.vert{font-family:"Roboto",Arial,sans-serif;font-weight:700;text-transform:uppercase;writing-mode:vertical-rl;transform:rotate(180deg);white-space:nowrap}
.about-vert{left:160px;top:812px;font-size:40px;color:rgba(255,255,255,.8)}
.about-title{left:666px;top:812px;font-size:46px;color:var(--ink)}
.para{font-size:14px;line-height:19.3px;color:var(--ink)}
.about-text{left:666px;top:887px;width:385px}
.about-btn{left:666px;top:1153px;width:144px;height:40px;font-size:15px;font-weight:700}
/* why */
.why-dark{left:0;top:1306px;width:618px;height:559px;background:var(--navy)}
.why-photo{left:618px;top:1384px;width:582px;height:481px;background:linear-gradient(150deg,#2b2e35,#6b0d12 45%,#d11e28 70%,#3a0a0c)}
.why-ghost{left:648px;top:1310px;font-size:44px;color:#eeeeee}
.why-title{left:149px;top:1368px;font-size:46px;color:var(--white)}
.why-text{left:149px;top:1435px;width:430px;font-size:14px;line-height:19px;color:var(--white)}
.why-item{left:152px;width:440px;color:var(--white)}
.why-num{position:absolute;left:0;top:0;width:60px;height:60px;border-radius:50%;background:var(--red);border:4px solid #7a1216;display:flex;align-items:center;justify-content:center;font-family:"Roboto",Arial,sans-serif;font-weight:700;font-size:24px}
.why-item h3{position:absolute;left:86px;top:-6px;font-family:"Roboto",Arial,sans-serif;font-size:20px;font-weight:500;white-space:nowrap}
.why-item p{position:absolute;left:88px;top:30px;width:330px;font-size:12.5px;line-height:17px}
/* services */
.section-title{left:0;width:1200px;text-align:center;font-size:46px;color:var(--ink)}
.svc{width:280px;text-align:center}
.svc-icon{position:absolute;left:65px;top:0;width:150px;height:150px;border-radius:50%;background:var(--light);display:flex;align-items:center;justify-content:center}
.svc-icon svg{width:78px;height:78px}
.svc h3{position:absolute;left:0;top:170px;width:280px;font-family:"Roboto",Arial,sans-serif;font-weight:500;font-size:22px}
.svc p{position:absolute;left:0;top:207px;width:280px;font-size:13.5px;line-height:18.5px;color:var(--grey)}
/* reviews */
.rev-bg{left:0;top:2782px;width:1200px;height:444px;background:var(--light)}
.rev-red{left:0;top:2782px;width:505px;height:444px;background:linear-gradient(135deg,#e2242d,#c81d25);border-top-right-radius:52px}
.rev-vert{left:132px;top:2826px;font-size:40px;color:rgba(255,255,255,.28)}
.rev-photo{left:285px;top:2858px;width:256px;height:289px;border:2px solid var(--red);background:linear-gradient(180deg,#e9eaee,#c8cad0)}
.rev-title{left:601px;top:2860px;font-size:44px;color:var(--ink)}
.quote-mark{left:601px;top:2930px}
.rev-text{left:603px;top:2985px;width:445px;font-style:italic;font-size:14px;line-height:19.5px;color:var(--ink)}
.rev-name{left:603px;top:3075px;font-family:"Roboto",Arial,sans-serif;font-weight:500;color:var(--red);font-size:22px}
.rev-role{left:622px;top:3106px;font-size:14px;color:var(--grey)}
.dots-nav{left:622px;top:3142px;display:flex;gap:4px}
.dots-nav i{display:block;width:14px;height:14px;border-radius:50%;border:1.5px solid #999}
.dots-nav i.on{background:var(--red);border-color:var(--red)}
/* news */
.card{border:2px solid #cfcfcf;background:var(--white)}
.news-big{left:154px;top:3408px;width:435px;height:476px}
.news-big .img{position:absolute;left:0;top:0;width:431px;height:270px;background:linear-gradient(120deg,#e6e7ea,#9aa0aa 55%,#3b3f47)}
.news-big h3{position:absolute;left:16px;top:295px;width:400px;font-family:"Roboto",Arial,sans-serif;font-weight:500;font-size:17.5px;line-height:21px}
.news-big p{position:absolute;left:16px;top:346px;width:400px;font-size:12.5px;line-height:16px;color:var(--grey)}
.more{font-family:"Roboto",Arial,sans-serif;font-weight:500;color:var(--red);text-decoration:underline;text-transform:uppercase}
.date{display:flex;align-items:center;gap:6px;font-size:12px;color:var(--grey)}
.news-small{left:611px;width:435px;height:225px}
.news-small .img{position:absolute;left:0;top:0;width:214px;height:221px}
.news-small .body{position:absolute;left:236px;top:18px;width:185px}
.news-small h3{font-family:"Roboto",Arial,sans-serif;font-weight:500;font-size:14.5px;line-height:18px}
.news-small p{margin-top:12px;font-size:12.5px;line-height:16px;color:var(--grey)}
/* footer */
.footer{left:0;top:3976px;width:1200px;height:337px;background:var(--navy)}
.f-brand{left:151px;top:4055px;color:var(--white)}
.f-brand small{color:var(--white)}
.social{top:4143px;width:40px;height:40px;border-radius:50%;border:2px solid var(--red)}
.f-col h4{font-family:"Roboto",Arial,sans-serif;font-weight:500;font-size:22px;color:var(--white);margin-bottom:22px}
.f-col li{list-style:none;font-size:12.5px;line-height:22.5px;color:var(--white)}
.contact-row{display:flex;align-items:flex-start;gap:12px;font-size:12.5px;line-height:15px;color:var(--white);margin-bottom:18px}
.contact-row .ic{flex:0 0 28px;width:28px;height:28px;border-radius:50%;background:var(--red);display:flex;align-items:center;justify-content:center}
.f-rule{left:0;top:4257px;width:1200px;height:1px;background:#2a3048}
.copy{left:0;top:4278px;width:1200px;text-align:center;font-size:12.5px;color:var(--white)}
</style>
</head>
<body>

<!-- Header -->
<div class="abs topbar"></div>
<div class="abs brand" style="left:151px;top:34px">CORVEX<small>AUTO REPAIR</small></div>
<div class="btn" style="left:879px;top:17px;width:171px;height:42px;font-size:17px">Get a Quote</div>
<nav class="abs nav" style="left:0;top:80px;width:1200px">
  <span style="left:524px;color:var(--red)">Home</span>
  <span style="left:598px">About Us</span>
  <span style="left:696px">Services</span>
  <span style="left:793px">Vehicles</span>
  <span style="left:891px">Reviews</span>
  <span style="left:983px">Contact</span>
</nav>

<!-- Hero -->
<div class="abs hero-red"></div>
<div class="photo hero-photo" role="img" aria-label="Smiling mechanic holding a wrench in front of a red car with its bonnet open"></div>
<h1 class="abs head hero-title">Best Automotive<br>Repair Shop<br>in California</h1>
<div class="btn hero-btn">Make an Appointment</div>

<!-- About -->
<div class="abs dots"></div>
<div class="photo about-big" role="img" aria-label="Technician in red gloves carrying a tyre beside a silver car"></div>
<div class="photo about-small" role="img" aria-label="Detailer polishing the bonnet of a red car"></div>
<div class="abs vert about-vert">About Us</div>
<h2 class="abs head about-title"><span class="hl">About</span> Us</h2>
<p class="abs para about-text">Lorem ipsum dolor sit amet, consectetur adipiscing elit, sed do eiusmod tempor incididunt ut labore et dolore magna aliqua. Ut enim ad minim veniam, quis nostrud exercitation ullamco laboris nisi ut aliquip ex ea commodo consequat. Duis aute irure dolor in reprehenderit in voluptate velit esse cillum dolore eu fugiat nulla pariatur. Excepteur sint occaecat cupidatat non proident, sunt in culpa qui officia deserunt mollit anim id est laborum.Sed ut perspiciatis unde omnis iste natus error sit voluptatem accusantium doloremque laudantium, totam rem aperiam, eaque ipsa quae ab illo inventore veritatis et quasisunt explicabo.</p>
<div class="btn about-btn">Read More</div>

<!-- Why choose us -->
<div class="abs why-dark"></div>
<div class="abs head why-ghost">Why Choose Us?</div>
<div class="photo why-photo" role="img" aria-label="Gloved hands polishing the headlight of a red car"></div>
<h2 class="abs head why-title"><span class="hl">Why Choose</span> Us?</h2>
<p class="abs why-text">Lorem ipsum dolor sit amet, consectetur adipiscing elit, sed do eiusmod tempor incididunt ut labore et dolore magna aliqua.</p>
<div class="abs why-item" style="top:1507px"><div class="why-num">01</div><h3>Proffesional Staff</h3><p>Lorem ipsum dolor sit amet, consectetur adipiscing elit, sed do eiusmod tempor&nbsp; dolore magna aliqua.</p></div>
<div class="abs why-item" style="top:1607px"><div class="why-num">02</div><h3>Proffesional Staff</h3><p>Lorem ipsum dolor sit amet, consectetur adipiscing elit, sed do eiusmod tempor&nbsp; dolore magna aliqua.</p></div>
<div class="abs why-item" style="top:1708px"><div class="why-num">03</div><h3>Proffesional Staff</h3><p>Lorem ipsum dolor sit amet, consectetur adipiscing elit, sed do eiusmod tempor&nbsp; dolore magna aliqua.</p></div>

<!-- Services -->
<h2 class="abs head section-title" style="top:1945px"><span class="hl">Our</span> Services</h2>

<div class="abs svc" style="left:141px;top:2069px">
  <div class="svc-icon" role="img" aria-label="Oil can icon"><svg viewBox="0 0 80 80"><path d="M10 44h36l16-12 8 4-18 20H16z" fill="var(--red)"/><rect x="26" y="34" width="12" height="10" fill="var(--red)"/><path d="M12 58c0 4 4 8 0 12-4-4 0-8 0-12z" fill="var(--red)"/></svg></div>
  <h3>Change Oil &amp; Filter</h3>
  <p>Lorem ipsum dolor sit amet, consectetur adipiscing elit, sed do eiusmod tempor incididunt ut labore et dolore aliqua.</p>
</div>
<div class="abs svc" style="left:460px;top:2069px">
  <div class="svc-icon" role="img" aria-label="Car battery icon"><svg viewBox="0 0 80 80"><rect x="14" y="18" width="12" height="8" fill="var(--red)"/><rect x="54" y="18" width="12" height="8" fill="var(--red)"/><rect x="8" y="24" width="64" height="12" fill="var(--red)"/><rect x="12" y="38" width="56" height="30" fill="var(--red)"/><path d="M42 42l-10 14h8l-4 10 12-15h-8z" fill="#fff"/></svg></div>
  <h3>Battery Replacement</h3>
  <p>Lorem ipsum dolor sit amet, consectetur adipiscing elit, sed do eiusmod tempor incididunt ut labore et dolore aliqua.</p>
</div>
<div class="abs svc" style="left:777px;top:2069px">
  <div class="svc-icon" role="img" aria-label="Transmission gears icon"><svg viewBox="0 0 80 80"><rect x="8" y="16" width="64" height="8" fill="var(--red)"/><rect x="12" y="26" width="14" height="40" rx="3" fill="var(--red)"/><rect x="33" y="26" width="14" height="40" rx="3" fill="var(--red)"/><rect x="54" y="26" width="14" height="40" rx="3" fill="var(--red)"/><rect x="8" y="42" width="64" height="6" fill="var(--red)"/></svg></div>
  <h3>Clutch &amp; Transmission</h3>
  <p>Lorem ipsum dolor sit amet, consectetur adipiscing elit, sed do eiusmod tempor incididunt ut labore et dolore aliqua.</p>
</div>

<div class="abs svc" style="left:141px;top:2408px">
  <div class="svc-icon" role="img" aria-label="Car on a diagnostic lift icon"><svg viewBox="0 0 80 80"><circle cx="40" cy="40" r="38" fill="var(--red)"/><path d="M22 42l5-12h26l5 12v8H22z" fill="none" stroke="#fff" stroke-width="3"/><line x1="40" y1="50" x2="40" y2="62" stroke="#fff" stroke-width="3"/><line x1="30" y1="64" x2="50" y2="64" stroke="#fff" stroke-width="3"/></svg></div>
  <h3>Car Diagnostics</h3>
  <p>Lorem ipsum dolor sit amet, consectetur adipiscing elit, sed do eiusmod tempor incididunt ut labore et dolore aliqua.</p>
</div>
<div class="abs svc" style="left:460px;top:2408px">
  <div class="svc-icon" role="img" aria-label="Wheel rim icon"><svg viewBox="0 0 80 80"><circle cx="40" cy="40" r="38" fill="var(--red)"/><circle cx="40" cy="40" r="24" fill="none" stroke="#fff" stroke-width="4"/><circle cx="40" cy="40" r="6" fill="#fff"/><path d="M40 16v48M16 40h48M23 23l34 34M57 23L23 57" stroke="#fff" stroke-width="3"/></svg></div>
  <h3>Tire Installation</h3>
  <p>Lorem ipsum dolor sit amet, consectetur adipiscing elit, sed do eiusmod tempor incididunt ut labore et dolore aliqua.</p>
</div>
<div class="abs svc" style="left:777px;top:2408px">
  <div class="svc-icon" role="img" aria-label="Brake disc and pad icon"><svg viewBox="0 0 80 80"><circle cx="36" cy="44" r="32" fill="var(--red)"/><circle cx="36" cy="44" r="20" fill="none" stroke="#fff" stroke-width="3"/><circle cx="36" cy="44" r="5" fill="#fff"/><rect x="50" y="4" width="22" height="26" rx="4" transform="rotate(30 61 17)" fill="var(--red)" stroke="#fff" stroke-width="2"/></svg></div>
  <h3>Brake Pads Replacement</h3>
  <p>Lorem ipsum dolor sit amet, consectetur adipiscing elit, sed do eiusmod tempor incididunt ut labore et dolore aliqua.</p>
</div>

<!-- Reviews -->
<div class="abs rev-bg"></div>
<div class="abs rev-red" role="img" aria-label="Red-tinted workshop background"></div>
<div class="abs vert rev-vert">Client Reviews</div>
<div class="photo rev-photo" role="img" aria-label="Portrait of a smiling customer with arms crossed"></div>
<h2 class="abs head rev-title"><span class="hl">Client</span> Reviews</h2>
<svg class="abs quote-mark" width="42" height="34" viewBox="0 0 42 34"><path d="M2 32V18C2 8 8 2 17 1v6c-5 1-7 4-7 9h7v16zM25 32V18c0-10 6-16 15-17v6c-5 1-7 4-7 9h7v16z" fill="#777"/></svg>
<p class="abs rev-text">Lorem ipsum dolor sit amet, consectetur adipiscing elit, sed do eiusmod tempor incididunt ut labore et dolore magna aliqua. Ut enim ad minim veniam, quis nostrud exercitation ullamco laboris nisi ut aliquip ex ea commodo consequat.</p>
<div class="abs rev-name">- Dane Morrow</div>
<div class="abs rev-role">Lorem Ipsum</div>
<div class="abs dots-nav"><i class="on"></i><i></i><i></i><i></i><i></i><i></i></div>

<!-- News -->
<h2 class="abs head section-title" style="top:3315px"><span class="hl">Latest</span> News</h2>

<article class="abs card news-big">
  <div class="img" role="img" aria-label="Mechanic with a laptop beside an open engine bay"></div>
  <h3>Lorem ipsum dolor sit amet, consectetur&nbsp; dolor incididunt ut lalore magna aliqua.</h3>
  <p>Lorem ipsum dolor sit amet, consectetur adipiscing elit, sed do eiusmod tempor incididunt ut labore et dolore magna aliqua. Ut enim ad minim veniam, qurconsequat.</p>
  <span class="abs more" style="left:16px;top:427px;font-size:14px">Read More</span>
  <span class="abs date" style="left:282px;top:427px"><svg width="16" height="16" viewBox="0 0 16 16"><rect x="1" y="3" width="14" height="12" fill="var(--red)"/><rect x="4" y="1" width="2" height="4" fill="var(--red)"/><rect x="10" y="1" width="2" height="4" fill="var(--red)"/><path d="M3 8h10M3 11h10M6 6v8M10 6v8" stroke="#fff"/></svg>April 04, 2023</span>
</article>

<article class="abs card news-small" style="top:3408px">
  <div class="img" role="img" aria-label="Mechanic in red overalls working under a lifted car" style="background:linear-gradient(135deg,#2b2f38,#8a1a1f 60%,#d9dadd)"></div>
  <div class="body">
    <h3>Lorem ipsum dolor samet, consectetur adipis elit, sed do</h3>
    <p>Lorem ipsum dolor sit amet, consectetur adipiscing elit, incididunt u magna aliqua.</p>
    <span class="date" style="margin-top:14px"><svg width="16" height="16" viewBox="0 0 16 16"><rect x="1" y="3" width="14" height="12" fill="var(--red)"/><path d="M3 8h10M3 11h10M6 6v8M10 6v8" stroke="#fff"/></svg>April 04, 2023</span>
    <div class="more" style="margin-top:14px;font-size:12px">Read More</div>
  </div>
</article>

<article class="abs card news-small" style="top:3656px">
  <div class="img" role="img" aria-label="Gloved technician connecting wiring in an engine bay" style="background:linear-gradient(135deg,#1a1f2c,#4a5266 55%,#8a1a1f)"></div>
  <div class="body">
    <h3>Lorem ipsum dolor samet, consectetur adipis elit, sed do</h3>
    <p>Lorem ipsum dolor sit amet, consectetur adipiscing elit, incididunt u magna aliqua.</p>
    <span class="date" style="margin-top:14px"><svg width="16" height="16" viewBox="0 0 16 16"><rect x="1" y="3" width="14" height="12" fill="var(--red)"/><path d="M3 8h10M3 11h10M6 6v8M10 6v8" stroke="#fff"/></svg>April 04, 2023</span>
    <div class="more" style="margin-top:14px;font-size:12px">Read More</div>
  </div>
</article>

<!-- Footer -->
<footer>
  <div class="abs footer"></div>
  <div class="abs brand f-brand">CORVEX<small>AUTO REPAIR</small></div>
  <div class="abs social" style="left:174px"></div>
  <div class="abs social" style="left:223px"></div>
  <div class="abs social" style="left:270px"></div>

  <div class="abs f-col" style="left:495px;top:4052px;width:200px">
    <h4>Get In Touch</h4>
    <div class="contact-row"><span class="ic"><svg width="14" height="16" viewBox="0 0 14 16"><path d="M7 0a6 6 0 0 0-6 6c0 4 6 10 6 10s6-6 6-10a6 6 0 0 0-6-6z" fill="#fff"/><circle cx="7" cy="6" r="2.2" fill="var(--red)"/></svg></span><span>123 ipsum dolor sit<br>amet, st:123/4</span></div>
    <div class="contact-row" style="align-items:center"><span class="ic"><svg width="14" height="14" viewBox="0 0 14 14"><path d="M3 1l2 3-1.5 1.5a8 8 0 0 0 5 5L10 9l3 2-1.5 2.5C6 13 1 8 .5 2.5z" fill="#fff"/></svg></span><span>888 888 8888</span></div>
    <div class="contact-row" style="align-items:center"><span class="ic"><svg width="14" height="11" viewBox="0 0 14 11"><rect x="0" y="0" width="14" height="11" rx="1" fill="#fff"/><path d="M0 1l7 5 7-5" fill="none" stroke="var(--red)" stroke-width="1.5"/></svg></span><span>info@corvexauto.example</span></div>
  </div>

  <div class="abs f-col" style="left:758px;top:4052px">
    <h4>Explore</h4>
    <ul><li>Home</li><li>About</li><li>Our Services</li><li>Vehicles</li><li>Reviews</li><li>Contact</li></ul>
  </div>

  <div class="abs f-col" style="left:947px;top:4052px">
    <h4>Policies</h4>
    <ul><li>Privacy Policy</li><li>Terms &amp; Conditions</li><li>Legal</li><li>Cookie</li></ul>
  </div>

  <div class="abs f-rule"></div>
  <div class="abs copy">© 2023 Corvex Auto Repair. All rights reserved</div>
</footer>

</body>
</html>
```